Melvin Otrasko Consulting Corporation
Independent Insurance and Reinsurance Consultants
Melvin Otrasko Consulting Corporation - Consulting
Creative Brief
Professional
Melvin Otrasko, MBA, CPCU
Insurance and Reinsurance Consultant
3816C Verlune Court Carlsbad, CA 92011
motrasko@motraskoadvise.com
www.motraskoadvise.com

```html
<!DOCTYPE html>
<html lang="en">
<head>
<meta charset="utf-8">
<title>Melvin Otrasko Consulting Corporation – Business Cards</title>
<link href="https://fonts.googleapis.com/css2?family=Marcellus&family=Open+Sans:wght@400;600;700&display=swap" rel="stylesheet">
<style>
  :root {
    --bg: #dcdcdc;
    --card-white: #ffffff;
    --brand-blue: #1f5fb5;
    --deep-blue: #0e4fa6;
    --mid-blue: #2c7fd3;
    --ink: #333333;
    --rule: #9aa7b8;
    --ghost: rgba(150,160,170,0.20);
  }
  * { box-sizing: border-box; margin: 0; padding: 0; }
  html, body { width: 1200px; height: 794px; overflow: hidden; }
  body { background: var(--bg); font-family: "Open Sans", Arial, sans-serif; position: relative; }

  .card {
    position: absolute;
    border-radius: 20px;
    overflow: hidden;
    box-shadow: 0 2px 6px rgba(0,0,0,0.18);
  }
  .card--front { left: 319px; top: 29px; width: 557px; height: 322px; background: var(--card-white); }
  .card--back-light { left: 29px; top: 427px; width: 528px; height: 305px; background: var(--card-white); }
  .card--back-dark {
    left: 593px; top: 427px; width: 528px; height: 305px;
    background: radial-gradient(ellipse at 45% 40%, var(--mid-blue) 0%, var(--deep-blue) 70%, #0a3f8a 100%);
  }

  .wave { position: absolute; left: 0; top: 0; width: 100%; height: 130px; }

  .emblem-area {
    position: absolute;
    border-radius: 50% 50% 12% 12%;
    background: radial-gradient(ellipse at 50% 45%, var(--ghost) 0%, rgba(150,160,170,0.07) 60%, transparent 75%);
  }
  .card--front .emblem-area { left: 40px; top: 130px; width: 180px; height: 190px; }
  .card--back-light .emblem-area { left: 60px; top: 15px; width: 210px; height: 280px; }
  .card--back-dark .emblem-area {
    left: 180px; top: 15px; width: 210px; height: 280px;
    background: radial-gradient(ellipse at 50% 45%, rgba(120,200,230,0.25) 0%, rgba(120,200,230,0.07) 60%, transparent 75%);
  }

  .company-name {
    font-family: "Marcellus", Georgia, serif;
    color: var(--brand-blue);
    font-weight: 400;
    line-height: 1;
    white-space: nowrap;
  }
  .company-sub {
    font-family: "Open Sans", Arial, sans-serif;
    color: var(--brand-blue);
    font-weight: 400;
    white-space: nowrap;
  }

  .front-brand { position: absolute; left: 30px; top: 72px; }
  .front-brand .company-name { font-size: 31px; }
  .front-brand .company-sub { font-size: 13px; letter-spacing: 2.6px; margin-top: 4px; }

  .person { position: absolute; left: 36px; top: 208px; }
  .person-name { font-weight: 700; font-size: 15.5px; color: var(--brand-blue); white-space: nowrap; }
  .person-role { font-size: 11.5px; color: var(--ink); margin-top: 3px; }

  .divider { position: absolute; left: 290px; top: 160px; width: 1px; height: 150px; background: var(--rule); }

  .contact { position: absolute; left: 302px; top: 160px; font-size: 12px; color: var(--ink); line-height: 19px; }
  .contact address { font-style: normal; margin-bottom: 8px; }
  .contact ul { list-style: none; }
  .contact li { display: flex; align-items: center; gap: 6px; white-space: nowrap; }
  .contact svg { width: 11px; height: 11px; flex: none; }

  .back-brand { position: absolute; left: 0; right: 0; top: 140px; text-align: center; }
  .back-brand .company-name { font-size: 30px; }
  .back-brand .company-sub { font-size: 13px; letter-spacing: 2.6px; margin-top: 4px; }
  .card--back-dark .company-name, .card--back-dark .company-sub { color: #ffffff; }

  .back-web {
    position: absolute; left: 0; right: 0; bottom: 16px;
    text-align: center; font-size: 11.5px; font-weight: 600; color: var(--ink);
  }
  .card--back-dark .back-web { color: #ffffff; }
</style>
</head>
<body>

  <section class="card card--front" aria-label="Business card front">
    <svg class="wave" viewBox="0 0 557 130" preserveAspectRatio="none" aria-hidden="true">
      <defs>
        <linearGradient id="band" x1="0" y1="0" x2="1" y2="0">
          <stop offset="0" stop-color="#1f64bf"/>
          <stop offset="0.6" stop-color="#2d86d8"/>
          <stop offset="1" stop-color="#0f4ea3"/>
        </linearGradient>
      </defs>
      <path d="M0 0 H557 V112 C480 106 430 58 320 38 C220 22 100 26 0 34 Z" fill="url(#band)"/>
      <path d="M0 40 C110 30 230 28 330 46 C430 64 490 108 557 120 V126 C480 116 425 78 325 58 C225 38 110 40 0 48 Z" fill="#5aa9e8" opacity="0.55"/>
    </svg>

    <div class="emblem-area" role="img" aria-label="Faint scales of justice emblem"></div>

    <div class="front-brand">
      <div class="company-name">MELVIN OTRASKO</div>
      <div class="company-sub">CONSULTING CORPORATION</div>
    </div>

    <div class="person">
      <div class="person-name">Melvin Otrasko, MBA, CPCU</div>
      <div class="person-role">Insurance and Reinsurance Consultant</div>
    </div>

    <div class="divider"></div>

    <div class="contact">
      <address>3816C Verlune Court<br>Carlsbad, CA 92011</address>
      <ul>
        <li><svg viewBox="0 0 12 12"><path d="M3 1 L5 3.5 L4 5 C4.8 6.6 5.6 7.4 7 8 L8.5 7 L11 9 L9.8 11 C5 10.5 1.5 7 1 2.2 Z" fill="#555"/></svg>6195550182</li>
        <li><svg viewBox="0 0 12 12"><rect x="3" y="0.5" width="6" height="11" rx="1.2" fill="#555"/><rect x="4" y="2" width="4" height="6" fill="#fff"/></svg>6195550147</li>
        <li><svg viewBox="0 0 12 12"><rect x="1" y="4" width="10" height="7" rx="1" fill="#555"/><rect x="3" y="1" width="6" height="4" fill="#777"/><rect x="3" y="7" width="6" height="1.5" fill="#fff"/></svg>7605550129</li>
        <li><svg viewBox="0 0 12 12"><circle cx="6" cy="6" r="5.5" fill="#555"/><path d="M3 4.2 H9 V8 H3 Z M3 4.2 L6 6.5 L9 4.2" fill="none" stroke="#fff" stroke-width="0.9"/></svg>motrasko@motraskoadvise.com</li>
        <li><svg viewBox="0 0 12 12"><circle cx="6" cy="6" r="5.5" fill="#555"/><ellipse cx="6" cy="6" rx="2.3" ry="5" fill="none" stroke="#fff" stroke-width="0.8"/><path d="M1 6 H11" stroke="#fff" stroke-width="0.8"/></svg>www.motraskoadvise.com</li>
      </ul>
    </div>
  </section>

  <section class="card card--back-light" aria-label="Business card back, white">
    <div class="emblem-area" role="img" aria-label="Faint scales of justice emblem"></div>
    <div class="back-brand">
      <div class="company-name">MELVIN OTRASKO</div>
      <div class="company-sub">CONSULTING CORPORATION</div>
    </div>
    <div class="back-web">www.motraskoadvise.com</div>
  </section>

  <section class="card card--back-dark" aria-label="Business card back, blue">
    <div class="emblem-area" role="img" aria-label="Faint scales of justice emblem"></div>
    <div class="back-brand">
      <div class="company-name">MELVIN OTRASKO</div>
      <div class="company-sub">CONSULTING CORPORATION</div>
    </div>
    <div class="back-web">www.motraskoadvise.com</div>
  </section>

</body>
</html>
```